Fashion-Forward Baby Dummy (Pacifier) Requires Safety Information Card to insert into Packaging

I am about to go to market with my gorgeous, fashionable baby dummies and matching chains/clips.

The brand is called Pruvelle, and it's aimed at the fashion-conscious baby (and parents). This is a brand new company, created by me, and five years in the making (it's taken that long to find the right factory to produce the dummies exactly the way I imagined them)!

The website isn't live yet, but is www.pruvelle-example.com

The initial release is five dummies with matching chains and clips, which are bright, edgy and designed to coordinate with the super-cool gear that babies wear these days. I have hundreds more designs to follow, with plans to expand into clothing and other accessories.

I need a safety information card to fit inside a clear plastic cube. It needs to measure:

7cms x 7cms square (when folded in half).
7cms x 14cms when unfolded/opened (landscape).

Logo on the front, critical safety information inside, and company information and web address on the back.

Target Market(s)

Parents aged 25 - 40+ who are educated, worldly, and fashion conscious. City dwellers, professionals.

Industry/Entity Type

Clothing

Requirements
Must have
• The Pruvelle logo must be on the front of the card. The Pantone colour is green 360C.

As dictated by the Safety Standard, the below text is compulsory for the centre (inside) of the folded card:

Pruvelle Baby Soother and Safety Chain
Instructions for hygenic care, safety & use

Please read before use:

WARNING - NEVER attach ribbons or cords to your soother. DO NOT TIE THE DUMMY AROUND YOUR BABY’S NECK AS IT PRESENTS A STRANGULATION HAZARD.
Inspect soother carefully before each use, especially when the child has teeth. Pull the soother in all directions. Throw away at the first sign of damage or weakness.
Use only under adult supervision.
Do not use abrasive or solvent-based cleaning agents as this may damage the soother. We suggest gentle washing before use in warm, soapy water and gentle towel-drying. Avoid scrubbing the printed surface as this will cause the design to fade. Remove any trapped water before use.
If a soother becomes lodged in the baby’s mouth DO NOT PANIC; it cannot be swallowed and is designed to cope with such an event. Remove from the mouth carefully and as gently as possible.
NEVER dip the teat in sweet substances such as syrups, honey or jam, or medications as this can lead to tooth decay.
NEVER try to disassemble the soother or safety chain.
When not in use keep the soother in a clean container and do not leave in direct sunlight, or near a heat source such as heaters, car interiors, dishwashers or sterilising solution as this may weaken the teat.
Replace the soother, irrespective of condition, after one to two months of use, for hygeine and safety reasons.

Pruvelle soothers are in conformity with the Australian Safety Standard AS2432-1991 and intended for use by babies aged 6 - 24 months of age.

Company details must be on the back of the card:

www.pruvelle-example.com
Proudly designed in Australia, and manufactured in China for Pruvelle Pty Ltd
PO Box 58
TARLOWE QLD 4183
AUSTRALIA

```html
<!DOCTYPE html>
<html lang="en">
<head>
<meta charset="utf-8">
<title>Pruvelle – Safety Information Card</title>
<link rel="stylesheet" href="https://fonts.googleapis.com/css2?family=Open+Sans:wght@400&family=Comfortaa:wght@400&family=Arimo:wght@400&display=swap">
<style>
  :root {
    --stage: #ececec;
    --brand-green: #66b32e;
    --card-dark: #2e2b2a;
    --ink-light: #ffffff;
    --ink-soft: rgba(255,255,255,0.06);
    --web-green: #7cc242;
  }
  html, body {
    margin: 0;
    width: 1200px;
    height: 1142px;
    overflow: hidden;
    background: var(--stage);
  }
  .card {
    position: absolute;
    left: 80px;
    top: 311px;
    width: 1040px;
    height: 520px;
    display: flex;
    box-shadow: 0 6px 18px rgba(0,0,0,0.18);
  }
  .card-front {
    position: relative;
    width: 476px;
    height: 100%;
    background: var(--brand-green);
  }
  .brand-dot {
    position: absolute;
    left: 141px;
    top: 88px;
    width: 176px;
    height: 176px;
    border-radius: 50%;
    background: var(--ink-light);
  }
  .front-name {
    position: absolute;
    left: 120px;
    top: 340px;
    margin: 0;
    font-family: "Open Sans", sans-serif;
    font-weight: 400;
    font-size: 76px;
    line-height: 1;
    color: var(--ink-light);
  }
  .card-back {
    position: relative;
    flex: 1;
    height: 100%;
    background: var(--card-dark);
    color: var(--ink-light);
  }
  .back-ring {
    position: absolute;
    left: 138px;
    top: 150px;
    width: 190px;
    height: 190px;
    border-radius: 50%;
    border: 26px solid var(--ink-soft);
  }
  .binding {
    position: absolute;
    left: 440px;
    top: 0;
  }
  .back-name {
    position: absolute;
    left: 74px;
    top: 24px;
    margin: 0;
    font-family: "Open Sans", sans-serif;
    font-weight: 400;
    font-size: 72px;
    line-height: 1;
  }
  .product-line {
    position: absolute;
    left: 80px;
    top: 106px;
    margin: 0;
    font-family: "Comfortaa", sans-serif;
    font-size: 21px;
  }
  .care-line {
    position: absolute;
    left: 80px;
    top: 134px;
    margin: 0;
    font-family: "Comfortaa", sans-serif;
    font-size: 15px;
  }
  .contact {
    position: absolute;
    left: 80px;
    top: 262px;
    margin: 0;
    font-family: "Arimo", sans-serif;
    font-style: normal;
    font-size: 21px;
    line-height: 25px;
  }
  .contact .web {
    color: var(--web-green);
    display: block;
    margin-bottom: 6px;
  }
</style>
</head>
<body>
  <div class="card">
    <section class="card-front">
      <div class="brand-dot"></div>
      <h1 class="front-name">pruvelle</h1>
    </section>
    <section class="card-back">
      <div class="back-ring"></div>
      <h2 class="back-name">pruvelle</h2>
      <p class="product-line">Baby Soother &amp; Safety Chain</p>
      <p class="care-line">Instructions for hygenic care, safety &amp; use</p>
      <address class="contact">
        <span class="web">www.pruvelle-example.com</span>
        Proudly designed in Australia,<br>
        and manufactured in China<br>
        for Pruvelle Pty Ltd<br>
        PO Box 58<br>
        TARLOWE QLD 4183<br>
        AUSTRALIA
      </address>
    </section>
    <svg class="binding" width="90" height="520" viewBox="0 0 90 520" aria-hidden="true">
      <g stroke="#ffffff" stroke-width="3" fill="none" stroke-linecap="round">
        <path d="M20 40 h40"/><path d="M20 75 h40"/><path d="M20 110 h40"/>
        <path d="M20 145 h40"/><path d="M20 180 h40"/><path d="M20 215 h40"/>
        <path d="M20 250 h40"/><path d="M20 285 h40"/><path d="M20 320 h40"/>
        <path d="M20 355 h40"/><path d="M20 390 h40"/><path d="M20 425 h40"/>
        <path d="M20 460 h40"/>
      </g>
      <g fill="#ffffff">
        <circle cx="62" cy="40" r="6"/><circle cx="62" cy="75" r="6"/><circle cx="62" cy="110" r="6"/>
        <circle cx="62" cy="145" r="6"/><circle cx="62" cy="180" r="6"/><circle cx="62" cy="215" r="6"/>
        <circle cx="62" cy="250" r="6"/><circle cx="62" cy="285" r="6"/><circle cx="62" cy="320" r="6"/>
        <circle cx="62" cy="355" r="6"/><circle cx="62" cy="390" r="6"/><circle cx="62" cy="425" r="6"/>
        <circle cx="62" cy="460" r="6"/>
      </g>
    </svg>
  </div>
</body>
</html>
```